A property investment company, looking to provide lovely sustainable homes for familys and individua

For a small investment business i am starting which will buy and refurbish unloved houses and apartments to rent out or resell. the company name is my family surname (HARGREAVE). <br/>i would like the design to be simple with maybe some emphasis on an ethical and sustainable/environmentally friendly approach with a branding of maybe trees blended with some houses and or apartments.<br/>The colours i like for this design would be mainly green on either a white or black background.
Target Market(s)
This business card is to be used for professional people such as estate agents
mortgage brokers, solicitors and trades people.
Industry/Entity Type
Real Estate
Contact Information for Business Card
owner/director-Martin hargreave
e-mail-martin@hvholdings.co.uk
website-hargreavehomeholdings.co.uk
mobile-07700945318
landline-02079460581
Look and feel

```html
<!DOCTYPE html>
<html lang="en">
<head>
<meta charset="utf-8">
<title>Hargreave business card</title>
<link href="https://fonts.googleapis.com/css2?family=Arimo:wght@400;700&family=Michroma&display=swap" rel="stylesheet">
<style>
  :root {
    --backdrop: #c9c9c9;
    --card-white: #ffffff;
    --brand-green: #4c9321;
    --ink: #1e1e1e;
    --shadow: rgba(0, 0, 0, 0.35);
  }
  html, body {
    margin: 0;
    padding: 0;
    width: 1200px;
    height: 802px;
    overflow: hidden;
    background: var(--backdrop);
  }
  .canvas {
    position: relative;
    width: 1200px;
    height: 802px;
  }
  .card {
    position: absolute;
    top: 274px;
    width: 442px;
    height: 265px;
    box-shadow: 2px 3px 6px var(--shadow);
    overflow: hidden;
  }
  .card-front {
    left: 136px;
    background: var(--card-white);
    font-family: "Arimo", Arial, sans-serif;
  }
  .card-back {
    left: 624px;
    background: var(--brand-green);
  }
  .holder-name {
    position: absolute;
    left: 33px;
    top: 54px;
    margin: 0;
    font-size: 16px;
    font-weight: 700;
    color: var(--brand-green);
  }
  .holder-role {
    position: absolute;
    left: 34px;
    top: 73px;
    margin: 0;
    font-size: 13px;
    color: var(--ink);
  }
  .contact-list {
    position: absolute;
    left: 33px;
    top: 104px;
    margin: 0;
    padding: 0;
    list-style: none;
    font-size: 13px;
    color: var(--ink);
  }
  .contact-list li {
    display: flex;
    align-items: center;
    gap: 4px;
    height: 18px;
  }
  .contact-icon {
    width: 14px;
    height: 14px;
    flex: none;
  }
  .postal-address {
    position: absolute;
    left: 33px;
    top: 180px;
    margin: 0;
    font-size: 13px;
    line-height: 16px;
    font-style: normal;
    color: var(--ink);
  }
  .front-wordmark {
    position: absolute;
    right: 20px;
    top: 112px;
    width: 200px;
    display: flex;
    align-items: center;
    justify-content: center;
    gap: 8px;
    font-family: "Michroma", sans-serif;
    font-size: 19px;
    color: var(--brand-green);
  }
  .mark-square {
    width: 12px;
    height: 12px;
    background: var(--brand-green);
  }
  .back-wordmark {
    position: absolute;
    inset: 0;
    display: flex;
    align-items: center;
    justify-content: center;
    font-family: "Michroma", sans-serif;
    font-size: 28px;
    color: var(--card-white);
  }
</style>
</head>
<body>
<main class="canvas">
  <section class="card card-front">
    <h1 class="holder-name">MARTIN HARGREAVE</h1>
    <p class="holder-role">Managing Director</p>
    <ul class="contact-list">
      <li>
        <svg class="contact-icon" viewBox="0 0 14 14" aria-hidden="true">
          <rect x="0.75" y="0.75" width="12.5" height="12.5" rx="2" fill="none" stroke="var(--brand-green)" stroke-width="1.5"/>
          <path d="M4 3.5 L5.5 3.5 L6 5.5 L5 6.3 Q6 8.2 7.8 9 L8.6 8 L10.5 8.5 L10.5 10 Q6.5 10.5 4 6 Z" fill="var(--brand-green)"/>
        </svg>
        07700 945318
      </li>
      <li>
        <svg class="contact-icon" viewBox="0 0 14 14" aria-hidden="true">
          <rect x="0.5" y="2.5" width="13" height="9" fill="var(--brand-green)"/>
          <path d="M0.5 2.5 L7 8 L13.5 2.5" fill="none" stroke="var(--card-white)" stroke-width="1.2"/>
        </svg>
        martin@hvholdings.co.uk
      </li>
      <li>
        <svg class="contact-icon" viewBox="0 0 14 14" aria-hidden="true">
          <circle cx="7" cy="7" r="6.2" fill="var(--brand-green)"/>
          <g fill="none" stroke="var(--card-white)" stroke-width="0.9">
            <ellipse cx="7" cy="7" rx="2.6" ry="6.2"/>
            <line x1="0.8" y1="7" x2="13.2" y2="7"/>
            <line x1="7" y1="0.8" x2="7" y2="13.2"/>
          </g>
        </svg>
        hargreavehomeholdings.co.uk
      </li>
    </ul>
    <address class="postal-address">14 Elmfield Road<br>London, SE15 3QT</address>
    <div class="front-wordmark"><span class="mark-square"></span>HARGREAVE</div>
  </section>

  <section class="card card-back">
    <div class="back-wordmark">HARGREAVE</div>
  </section>
</main>
</body>
</html>
```